TrelWave Agile Coaching Website

I need an updated website for www.trelwave-demo.com. I'm looking for a modern look. This is a professional site, but I don't want it to look "stuffy". It needs to have an element of fun and learning.

My services include:
Lean Agile Coaching
Lean Agile Training
Facilitation
Workshops
Consulting

Ideas this site should convey: collaboration, learning, teamwork, adaptability, flow, limited WIP, agility, Lean.

I would like to use some of my own photos and slide decks for content: http://www.deckshelf-example.net/mirabrecken/presentations

I would also like to include the WorkWeb recommendations I have from customers: https://www.workweb-example.com/in/mirabrecken

Examples of sites I like:
http://www.corvalpine-example.com
http://www.stridemoss-example.com

Target Market(s)

IT professionals, software development managers

Industry/Entity Type

It Company

Coding

Coded - Design and coding required

Font styles to use
Serif
Sans Serif

Requirements
Must have
• Original looking graphics and layout.
• My logo must be included in layout.
• Need to feature my blog content.
• Deliverable must be a WordPress theme that I can install.
• Responsive site.
Nice to have
• Use images from my slides on DeckShelf if they make sense.

```html
<!DOCTYPE html>
<html lang="en">
<head>
<meta charset="utf-8">
<title>TrelWave – Lean Agile Coaching</title>
<link rel="stylesheet" href="https://fonts.googleapis.com/css2?family=Roboto:wght@400;500;700&family=Raleway:wght@400;500;600;700&display=swap">
<style>
:root{
  --green:#17c13d;
  --green-dark:#12a833;
  --ink:#1d1d1d;
  --body:#555;
  --muted:#8a8a8a;
  --teal:#1fb8ae;
  --olive:#b3b31b;
  --ochre:#c58f1b;
  --night:#1b1d1e;
  --bar:#1a1a1a;
  --white:#fff;
}
*{box-sizing:border-box;margin:0;padding:0}
html,body{width:1200px;height:2757px;overflow:hidden}
body{position:relative;background:var(--white);font-family:'Raleway',sans-serif;color:var(--body)}

/* header */
.site-header{position:absolute;left:0;top:0;width:1200px;height:92px;background:var(--white);border-top:4px solid var(--green);z-index:3}
.brand{position:absolute;left:100px;top:22px;display:flex;align-items:center;gap:10px}
.brand-mark{width:16px;height:40px;background:var(--ink)}
.brand-name{font-family:'Roboto',sans-serif;font-weight:700;font-size:42px;letter-spacing:-1.5px;color:var(--ink);line-height:1}
.main-nav{position:absolute;left:476px;top:-4px;height:96px;display:flex}
.main-nav a{font-family:'Roboto',sans-serif;font-size:15px;color:#222;text-decoration:none;height:96px;line-height:96px;padding:0 27px}
.main-nav a.active{background:var(--green);color:var(--white);padding:0 28px;margin-right:6px}

/* hero */
.hero{position:absolute;left:0;top:92px;width:1200px;height:568px;overflow:hidden}
.hero-photo{position:absolute;inset:0;background:linear-gradient(180deg,#4d4f4c 0%,#3a3c3a 45%,#262725 100%)}
.hero-cut{position:absolute;left:0;bottom:0}
.hero-title{position:absolute;left:235px;top:134px;width:727px;height:63px;background:var(--green);color:var(--white);font-family:'Roboto',sans-serif;font-size:39px;text-align:center;line-height:63px}
.hero-sub{position:absolute;left:260px;top:226px;width:680px;text-align:center;color:var(--white);font-family:'Raleway',sans-serif;font-weight:600;font-size:22px;line-height:33px}
.hero-btn{position:absolute;left:538px;top:329px;width:124px;height:48px;border:2px solid var(--white);color:var(--white);font-family:'Roboto',sans-serif;font-size:16px;text-align:center;line-height:44px}
.hero-arrow{position:absolute;top:266px}

/* welcome */
.section-title{font-family:'Roboto',sans-serif;font-weight:500;font-size:32px;color:var(--ink);letter-spacing:-.5px}
.section-title span{color:var(--green)}
.welcome-title{position:absolute;left:99px;top:697px}
.welcome-rule{position:absolute;left:99px;top:745px;width:236px;height:2px;background:var(--ink)}
.welcome-text{position:absolute;left:99px;top:777px;width:752px;font-size:12.6px;line-height:22px;color:#444}
.welcome-text p+p{margin-top:12px}
.portrait{position:absolute;left:900px;top:785px;width:197px;height:195px;background:linear-gradient(160deg,#8a6a3f,#b7a17d 55%,#3b4557)}

/* service cards */
.service{position:absolute;top:1033px;width:318px;height:307px;color:var(--white);text-align:center}
.service.teal{left:99px;background:var(--teal)}
.service.olive{left:441px;background:var(--olive)}
.service.ochre{left:781px;background:var(--ochre)}
.service svg{position:absolute;left:129px;top:22px}
.service h3{position:absolute;left:0;right:0;top:115px;font-family:'Roboto',sans-serif;font-weight:500;font-size:20px}
.service p{position:absolute;left:18px;right:18px;top:157px;font-size:12.3px;line-height:24px}
.service .btn{position:absolute;left:110px;top:245px;width:99px;height:33px;background:#2b2b2b;font-family:'Roboto',sans-serif;font-size:13px;line-height:33px}

/* feed */
.feed-title{position:absolute;left:0;width:1200px;top:1375px;text-align:center}
.feed-rule{position:absolute;left:521px;top:1423px;width:92px;height:2px;background:var(--ink)}
.post{position:absolute;top:1470px;width:308px}
.post-photo{width:308px;height:212px;border:4px solid #d8d8d8}
.post h4{margin-top:28px;font-family:'Roboto',sans-serif;font-weight:500;font-size:18px;color:var(--ink)}
.post-meta{margin-top:14px;display:flex;gap:16px;font-family:'Roboto',sans-serif;font-size:12px;color:var(--green)}
.post-meta span{display:flex;align-items:center;gap:5px}
.post p{margin-top:10px;font-size:12.3px;line-height:22px;color:#444}
.post .btn{margin-top:22px;width:121px;height:42px;border:2px solid #2b2b2b;font-family:'Roboto',sans-serif;font-weight:500;font-size:13px;text-align:center;line-height:38px;color:#222}
.post .btn.solid{background:var(--green);border-color:var(--green);color:var(--white)}

/* feedback */
.feedback{position:absolute;left:0;top:1933px;width:1200px;height:430px;background:var(--night)}
.feedback-photo{position:absolute;inset:0;background:linear-gradient(90deg,#202222 0%,#2a2c2b 50%,#1c1d1d 100%)}
.feedback-title{position:absolute;left:0;width:1200px;top:36px;text-align:center;color:var(--white)}
.feedback-rule{position:absolute;left:533px;top:87px;width:134px;height:2px;background:var(--white)}
.review{position:absolute;top:150px;width:520px;color:var(--white)}
.avatar{position:absolute;left:0;top:0;width:118px;height:118px;border-radius:50%;border:4px solid var(--white);background:linear-gradient(160deg,#c9a27a,#8c6a4d)}
.quote{position:absolute;left:143px;top:12px;font-family:'Roboto',sans-serif;font-weight:700;font-size:46px;line-height:40px;color:var(--green)}
.review h5{position:absolute;left:175px;top:16px;font-family:'Roboto',sans-serif;font-weight:500;font-size:21px}
.review .who{position:absolute;left:175px;top:50px;font-size:13px;color:#ddd}
.review .stars{position:absolute;left:175px;top:76px;font-size:15px;letter-spacing:2px;color:var(--green)}
.review .text{position:absolute;left:0;top:144px;width:520px;font-size:12.5px;line-height:22px;color:#eee}

/* footer */
.site-footer{position:absolute;left:0;top:2306px;width:1200px;height:390px}
.site-footer svg.band{position:absolute;left:0;top:0}
.foot-col{position:absolute;top:104px;color:var(--white)}
.foot-col h6{font-family:'Roboto',sans-serif;font-weight:500;font-size:16px;letter-spacing:.5px;margin-bottom:20px}
.foot-col li{list-style:none;font-size:13.5px;font-weight:500;height:31.5px}
.foot-col.posts li{display:flex;gap:12px;width:275px;height:auto;margin-bottom:12px;line-height:22px}
.foot-col.posts li svg{flex:none;margin-top:3px}
.contact-item{display:flex;gap:16px;margin-bottom:18px;font-size:12.5px;line-height:18px}
.contact-item strong{display:block;font-family:'Roboto',sans-serif;font-size:14px}
.ring{flex:none;width:38px;height:38px;border-radius:50%;border:2px solid var(--white);display:flex;align-items:center;justify-content:center}

.bottom-bar{position:absolute;left:0;top:2696px;width:1200px;height:61px;background:var(--bar);color:var(--white)}
.copyright{position:absolute;left:99px;top:22px;font-size:13px}
.social{position:absolute;top:12px;width:36px;height:36px;border-radius:50%;border:2px solid var(--white)}
</style>
</head>
<body>

<header class="site-header">
  <div class="brand"><div class="brand-mark"></div><div class="brand-name">TrelWave</div></div>
  <nav class="main-nav">
    <a class="active">HOME</a><a>ABOUT</a><a>SERVICES</a><a>NEWS</a><a>BLOG</a><a>CONTACT</a>
  </nav>
</header>

<section class="hero">
  <div class="hero-photo" role="img" aria-label="Team gathered around a table planning work with sticky notes and cards"></div>
  <div class="hero-title">“Clarity, Understanding, Improvement"</div>
  <div class="hero-sub">Improving software development through alignment, visibility,<br>knowledge, and discipline.</div>
  <div class="hero-btn">Read More</div>
  <svg class="hero-arrow" style="left:34px" width="22" height="50" viewBox="0 0 22 50"><polyline points="20,2 2,25 20,48" fill="none" stroke="#fff" stroke-width="2"/></svg>
  <svg class="hero-arrow" style="left:1144px" width="22" height="50" viewBox="0 0 22 50"><polyline points="2,2 20,25 2,48" fill="none" stroke="#fff" stroke-width="2"/></svg>
  <svg class="hero-cut" width="1200" height="56" viewBox="0 0 1200 56"><polygon points="0,2 600,54 1200,2 1200,56 0,56" fill="#fff"/></svg>
</section>

<h2 class="section-title welcome-title">Welcome To <span>trelwave</span></h2>
<div class="welcome-rule"></div>
<div class="welcome-text">
  <p>TrelWave is a company dedicated to improving the art and science of software development for both the consumers of software services and the professionals doing the work. Our primary focus is the marketplace and community where we live–the Harbor City metro area. Our specialty is helping software organizations learn about and implement Lean-Agile approaches to software development. This includes Kanban, Scrum and Agile team practices, and XP technical practices.</p>
  <p>Mira Brecken, LFC, is the owner and a principal consultant at TrelWave. She is a practicing Agilist and Lean-Agile coach to software teams, project managers and executives. She helps software professionals and teams improve through approaches that support better clarity, understanding, and continuous learning. Mira is the founder of the Harbor City Capped Queue Circle and is a regular speaker on topics of Lean, Agile, and Kanban.</p>
</div>
<div class="portrait" role="img" aria-label="Portrait of the principal consultant"></div>

<div class="service teal">
  <svg width="60" height="70" viewBox="0 0 60 70" fill="none" stroke="#fff" stroke-width="3"><circle cx="30" cy="30" r="26"/><circle cx="30" cy="26" r="8" fill="#fff"/><path d="M14 52c3-10 9-14 16-14s13 4 16 14" fill="#fff"/></svg>
  <h3>Lean Agile Coaching</h3>
  <p>Knowledge work endeavors such as software development projects seem anything but clear when in process.</p>
  <div class="btn">Read More</div>
</div>
<div class="service olive">
  <svg width="60" height="70" viewBox="0 0 60 70" fill="none" stroke="#fff" stroke-width="3"><rect x="6" y="6" width="48" height="36"/><rect x="18" y="16" width="8" height="16" fill="#fff"/><line x1="30" y1="22" x2="44" y2="22"/><circle cx="12" cy="56" r="4" fill="#fff"/><circle cx="30" cy="56" r="4" fill="#fff"/><circle cx="48" cy="56" r="4" fill="#fff"/></svg>
  <h3>Lean Agile Training</h3>
  <p>Knowledge work endeavors such as software development projects seem anything but clear when in process.</p>
  <div class="btn">Read More</div>
</div>
<div class="service ochre">
  <svg width="60" height="70" viewBox="0 0 60 70" fill="#fff"><circle cx="32" cy="20" r="10"/><g stroke="#fff" stroke-width="5"><line x1="32" y1="4" x2="32" y2="36"/><line x1="16" y1="20" x2="48" y2="20"/><line x1="21" y1="9" x2="43" y2="31"/><line x1="43" y1="9" x2="21" y2="31"/></g><circle cx="32" cy="20" r="4" fill="#c58f1b"/><path d="M2 48h16l10 4h14c4 0 4 6 0 6H28l16 0 12-8c4-2 6 2 3 5L44 64H2z"/></svg>
  <h3>Workshops</h3>
  <p>Knowledge work endeavors such as software development projects seem anything but clear when in process.</p>
  <div class="btn">Read More</div>
</div>

<h2 class="section-title feed-title">Recent <span>Social Feed</span></h2>
<div class="feed-rule"></div>

<article class="post" style="left:99px">
  <div class="post-photo" role="img" aria-label="Person marking a flow board on a long table" style="background:linear-gradient(135deg,#8a6436,#c5b39a 55%,#3b5a86)"></div>
  <h4>Steady Loom</h4>
  <div class="post-meta"><span>■ 95,135</span><span>▦ Feb 22, 2015</span><span>● No Comments</span></div>
  <p>"High Performing Teams" &lt;- might be wrong focus. Maybe look at system enablement and you may find you already have them.</p>
  <div class="btn solid">READ MORE</div>
</article>
<article class="post" style="left:445px">
  <div class="post-photo" role="img" aria-label="Speaker seated behind large yellow lettering on a red stage" style="background:linear-gradient(180deg,#c8323a 0%,#5a6c8c 55%,#c9a52a 75%,#b38a20 100%)"></div>
  <h4>Kanban can deliver make you mindful</h4>
  <div class="post-meta"><span>■ 95,135</span><span>▦ Feb 22, 2015</span><span>● No Comments</span></div>
  <p>For the uninitiated, I should start by explaining a little about Kanban. Kanban is a technique which focuses on delivering increased.</p>
  <div class="btn">READ MORE</div>
</article>
<article class="post" style="left:792px">
  <div class="post-photo" role="img" aria-label="Group meeting around lunch tables in an office" style="background:linear-gradient(160deg,#d7d2c4,#7d6e5c 50%,#3d3a36)"></div>
  <h4>CQC HC Monthly Overland</h4>
  <div class="post-meta"><span>■ 95,135</span><span>▦ Feb 22, 2015</span><span>● No Comments</span></div>
  <p>You're invited to join us for lunch and great conversation on Lean software and Kanban. This is a BYOL (bring your own lunch) event.</p>
  <div class="btn">READ MORE</div>
</article>

<section class="feedback">
  <div class="feedback-photo" role="img" aria-label="Darkened office interior with bookshelves"></div>
  <h2 class="section-title feedback-title">Customer <span>Feedbacks</span></h2>
  <div class="feedback-rule"></div>
  <div class="review" style="left:99px">
    <div class="avatar" role="img" aria-label="Customer portrait"></div>
    <div class="quote">“</div>
    <h5>Good trelwave</h5>
    <div class="who">Lorna Vey</div>
    <div class="stars">★★★★☆</div>
    <div class="text">Mira's breadth of experiences and knowledge provides her the insight to quickly understand organizational challenges.</div>
  </div>
  <div class="review" style="left:627px">
    <div class="avatar" role="img" aria-label="Customer portrait"></div>
    <div class="quote">“</div>
    <h5>Good trelwave</h5>
    <div class="who">Tomas Reld</div>
    <div class="stars">★★★★☆</div>
    <div class="text">I first met Mira at the Capped Queue Circle HC Meetings and found her to be a friendly and approachable with a deep understanding.</div>
  </div>
</section>

<footer class="site-footer">
  <svg class="band" width="1200" height="390" viewBox="0 0 1200 390"><polygon points="0,0 600,56 1200,0 1200,390 0,390" fill="#17c13d"/></svg>
  <div class="foot-col" style="left:99px">
    <h6>BLOG TOPICS</h6>
    <ul><li>› Education</li><li>› Flow</li><li>› Kanban</li><li>› Lean-Agile</li><li>› Minimum Viable Agile</li></ul>
  </div>
  <div class="foot-col" style="left:344px">
    <h6>QUICK LINKS</h6>
    <ul><li>› Home</li><li>› About Us</li><li>› Services</li><li>› Blog</li><li>› Contact Us</li></ul>
  </div>
  <div class="foot-col posts" style="left:531px">
    <h6>RECENT POSTS</h6>
    <ul>
      <li><svg width="16" height="16" viewBox="0 0 16 16"><circle cx="8" cy="8" r="8" fill="#fff"/><polyline points="6,4 10,8 6,12" fill="none" stroke="#17c13d" stroke-width="2"/></svg>Speaking at FlowSummit 2016</li>
      <li><svg width="16" height="16" viewBox="0 0 16 16"><circle cx="8" cy="8" r="8" fill="#fff"/><polyline points="6,4 10,8 6,12" fill="none" stroke="#17c13d" stroke-width="2"/></svg>Learning to Learn: Does Your Agile Process Encourage Learning?</li>
      <li><svg width="16" height="16" viewBox="0 0 16 16"><circle cx="8" cy="8" r="8" fill="#fff"/><polyline points="6,4 10,8 6,12" fill="none" stroke="#17c13d" stroke-width="2"/></svg>Lean Agile HC Conference</li>
      <li><svg width="16" height="16" viewBox="0 0 16 16"><circle cx="8" cy="8" r="8" fill="#fff"/><polyline points="6,4 10,8 6,12" fill="none" stroke="#17c13d" stroke-width="2"/></svg>HCDC 2015 Minimum Viable Agile Talk</li>
    </ul>
  </div>
  <div class="foot-col" style="left:886px">
    <h6>CONTACT US</h6>
    <div class="contact-item"><div class="ring"><svg width="14" height="18" viewBox="0 0 14 18"><path d="M7 1a6 6 0 0 1 6 6c0 4-6 10-6 10S1 11 1 7a6 6 0 0 1 6-6z" fill="none" stroke="#fff" stroke-width="2"/><circle cx="7" cy="7" r="2" fill="#fff"/></svg></div><div><strong>TRELWAVE,</strong>Lindale, Ste 401<br>Ferncrest, Oregon 97000</div></div>
    <div class="contact-item"><div class="ring"><svg width="12" height="18" viewBox="0 0 12 18"><rect x="1" y="1" width="10" height="16" rx="2" fill="none" stroke="#fff" stroke-width="2"/><circle cx="6" cy="14" r="1.3" fill="#fff"/></svg></div><div><strong>PHONE:</strong>1800 555 0142</div></div>
    <div class="contact-item"><div class="ring"><svg width="18" height="14" viewBox="0 0 18 14"><rect x="1" y="1" width="16" height="12" fill="none" stroke="#fff" stroke-width="2"/><polyline points="1,1 9,8 17,1" fill="none" stroke="#fff" stroke-width="2"/></svg></div><div><strong>Mail:</strong>info@trelwave-demo.com</div></div>
  </div>
</footer>

<div class="bottom-bar">
  <div class="copyright">Copyright © 2016 trelwave. All Right Reserved</div>
  <div class="social" style="left:949px"></div>
  <div class="social" style="left:989px"></div>
  <div class="social" style="left:1028px"></div>
  <div class="social" style="left:1067px"></div>
</div>

</body>
</html>
```